Yard sign

I want it to look similar to this one,

change name to DRAVEK and submit new ideas

Also would like to improvise a bit. let's not make exactly the same thing

would like to change to: Connecticut #1 Company

also change phone to 203-555-0147
and website to
dravekllc.com

this is yard sign. size is 24' Width and 32' Height

Target Market(s)

Roof

Industry/Entity Type

Roofing

Requirements
Must have
• similar colors or add something new

```html
<!DOCTYPE html>
<html lang="en">
<head>
<meta charset="utf-8">
<title>Dravek Roofing Yard Sign</title>
<link href="https://fonts.googleapis.com/css2?family=Marcellus&family=Nunito:wght@800&family=Raleway:wght@500&display=swap" rel="stylesheet">
<style>
  :root {
    --sign-bg-light: #f2f2f2;
    --sign-bg-dark: #dcdcdc;
    --slate: #5f5f5f;
    --slate-dark: #4a4a4a;
    --roof-orange: #f29a26;
    --white: #ffffff;
  }
  html, body {
    margin: 0;
    padding: 0;
    overflow: hidden;
    background: #ffffff;
  }
  .yard-sign {
    position: relative;
    width: 835px;
    height: 1200px;
    overflow: hidden;
    background: radial-gradient(ellipse at 50% 42%, var(--sign-bg-light) 0%, var(--sign-bg-dark) 100%);
  }
  .web-band {
    position: absolute;
    left: 49px;
    top: 0;
    width: 737px;
    height: 104px;
    background: var(--roof-orange);
    border-radius: 0 0 22px 22px;
  }
  .web-address {
    position: absolute;
    left: 0;
    right: 0;
    top: 36px;
    margin: 0;
    text-align: center;
    font-family: "Raleway", sans-serif;
    font-weight: 500;
    font-size: 26px;
    line-height: 32px;
    letter-spacing: 0.6em;
    padding-left: 0.6em;
    color: var(--white);
  }
  .headline {
    position: absolute;
    left: 0;
    right: 0;
    top: 232px;
    margin: 0;
    text-align: center;
    font-family: "Marcellus", serif;
    font-weight: 400;
    font-size: 44px;
    line-height: 56px;
    color: var(--slate);
    letter-spacing: 0.04em;
  }
  .brand-name {
    position: absolute;
    left: 0;
    top: 330px;
    width: 835px;
    height: 200px;
  }
  .brand-name text {
    font-family: "Marcellus", serif;
    font-size: 200px;
    fill: var(--roof-orange);
  }
  .divider {
    position: absolute;
    left: 0;
    top: 580px;
    width: 835px;
    height: 20px;
  }
  .tagline {
    position: absolute;
    left: 0;
    right: 0;
    top: 630px;
    margin: 0;
    text-align: center;
    font-family: "Marcellus", serif;
    font-weight: 400;
    font-size: 46px;
    line-height: 56px;
    color: var(--slate);
    letter-spacing: 0.02em;
  }
  .contact-panel {
    position: absolute;
    left: 44px;
    top: 880px;
    width: 747px;
    height: 320px;
    background: var(--slate-dark);
    border-radius: 22px 22px 0 0;
    border-top: 10px solid var(--roof-orange);
    box-sizing: border-box;
  }
  .phone-icon {
    position: absolute;
    left: 340px;
    top: 44px;
    width: 66px;
    height: 56px;
  }
  .phone-number {
    position: absolute;
    left: 0;
    top: 134px;
    width: 747px;
    height: 100px;
  }
  .phone-number text {
    font-family: "Nunito", sans-serif;
    font-weight: 800;
    font-size: 94px;
    fill: var(--white);
  }
</style>
</head>
<body>
  <main class="yard-sign">
    <header class="web-band">
      <p class="web-address">WWW.DRAVEKLLC.COM</p>
    </header>

    <h1 class="headline">CONNECTICUT #1 COMPANY</h1>

    <svg class="brand-name" viewBox="0 0 835 200" aria-label="Dravek">
      <text x="417.5" y="180" text-anchor="middle" textLength="720" lengthAdjust="spacingAndGlyphs">DRAVEK</text>
    </svg>

    <svg class="divider" viewBox="0 0 835 20" aria-hidden="true">
      <line x1="110" y1="10" x2="380" y2="10" stroke="var(--roof-orange)" stroke-width="3"/>
      <rect x="409" y="2" width="16" height="16" fill="var(--roof-orange)" transform="rotate(45 417 10)"/>
      <line x1="455" y1="10" x2="725" y2="10" stroke="var(--roof-orange)" stroke-width="3"/>
    </svg>

    <p class="tagline">QUALITY YOU CAN TRUST</p>

    <section class="contact-panel">
      <svg class="phone-icon" viewBox="0 0 66 56" aria-label="Phone">
        <path d="M4 18 C4 6 62 6 62 18 L62 22 L48 22 L46 15 C38 12 28 12 20 15 L18 22 L4 22 Z" fill="var(--roof-orange)"/>
        <path d="M21 20 L45 20 L58 44 L58 54 L8 54 L8 44 Z" fill="var(--roof-orange)"/>
        <g fill="var(--slate-dark)">
          <rect x="25" y="30" width="4" height="4"/><rect x="31" y="30" width="4" height="4"/><rect x="37" y="30" width="4" height="4"/>
          <rect x="25" y="36" width="4" height="4"/><rect x="31" y="36" width="4" height="4"/><rect x="37" y="36" width="4" height="4"/>
          <rect x="25" y="42" width="4" height="4"/><rect x="31" y="42" width="4" height="4"/><rect x="37" y="42" width="4" height="4"/>
        </g>
      </svg>
      <svg class="phone-number" viewBox="0 0 747 100" aria-label="203-555-0147">
        <text x="373.5" y="86" text-anchor="middle" textLength="650" lengthAdjust="spacingAndGlyphs">203-555-0147</text>
      </svg>
    </section>
  </main>
</body>
</html>
```